New Business Card : Logo provided (black&red)

Use logo to ascertain colours.
Front of card :
Logo
Director : Gareth Pollwick
ABN : 48392057
T : 0458 702 136
E : kinetrixx@postnest.com
W : kinetrixxfitness.com.au

Back of card :
Outdoor Group Training
Ferndale Archers Club
42 Tillbrook Road
Westhaven WA 6027

Personal Training
Amberline Fitness Studio
518 Wrenhollow Street
Westhaven WA 6027

Logo's attached are low resolution apparently so will look into why that is and update as soon as I can.  

Logo's updated.

```html
<!DOCTYPE html>
<html lang="en">
<head>
<meta charset="utf-8">
<title>Kinetrixx Fitness – Business Card</title>
<link href="https://fonts.googleapis.com/css2?family=Jost:wght@400;600;700&display=swap" rel="stylesheet">
<style>
  :root {
    --brand-red: #e8322b;
    --brand-red-light: #f25a45;
    --ink: #2b2b2b;
    --ink-soft: #5a5a5a;
    --paper: #ffffff;
    --backdrop: #e6e4e0;
    --on-red: #ffffff;
  }
  * { box-sizing: border-box; margin: 0; padding: 0; }
  html, body {
    width: 1200px; height: 900px; overflow: hidden;
    background: var(--backdrop);
    font-family: "Jost", "Futura", sans-serif;
  }
  .sheet {
    width: 1200px; height: 900px;
    display: flex; flex-direction: column; align-items: center; justify-content: center;
    gap: 56px;
  }
  .card {
    position: relative;
    width: 580px; height: 352px;
    border-radius: 2px;
    box-shadow: 0 6px 18px rgba(0,0,0,.18);
    overflow: hidden;
  }
  /* Back of card */
  .card--back {
    background: radial-gradient(ellipse at 45% 40%, var(--brand-red-light) 0%, var(--brand-red) 65%);
    color: var(--on-red);
  }
  .brand-mark {
    position: absolute;
    display: flex; align-items: center; gap: 12px;
  }
  .brand-mark__dot {
    width: 34px; height: 34px; border-radius: 50%;
    flex: none;
  }
  .brand-mark__name {
    font-weight: 700; font-size: 30px; line-height: 1;
    letter-spacing: .5px;
  }
  .card--back .brand-mark { left: 66px; top: 128px; }
  .card--back .brand-mark__dot { background: var(--on-red); }
  .card--back .brand-mark__name { color: var(--on-red); }

  .venue {
    position: absolute;
    font-size: 14px; line-height: 1.3;
  }
  .venue__title { font-weight: 600; font-size: 15px; }
  .venue--studio { right: 42px; top: 38px; text-align: right; }
  .venue--outdoor { left: 42px; bottom: 36px; }

  /* Front of card */
  .card--front { background: var(--paper); color: var(--ink); }
  .card--front .brand-mark { left: 40px; top: 58px; }
  .card--front .brand-mark__dot { background: var(--brand-red); }
  .card--front .brand-mark__name { color: var(--ink); }

  .contact {
    position: absolute; left: 318px; top: 132px;
  }
  .contact__name { color: var(--brand-red); font-weight: 600; font-size: 17px; }
  .contact__role { color: var(--ink-soft); font-size: 15px; margin-bottom: 14px; }
  .contact__list { list-style: none; }
  .contact__item {
    display: flex; align-items: center; gap: 12px;
    font-size: 17px; color: var(--ink-soft); line-height: 1.35;
  }
  .contact__icon { width: 13px; height: 13px; flex: none; fill: var(--brand-red); }
  .abn {
    position: absolute; left: 40px; bottom: 34px;
    font-size: 15px; color: var(--ink); letter-spacing: .5px;
  }
</style>
</head>
<body>
<main class="sheet">

  <section class="card card--back" aria-label="Back of card">
    <div class="brand-mark">
      <span class="brand-mark__dot"></span>
      <span class="brand-mark__name">KINETRIXX FITNESS</span>
    </div>
    <div class="venue venue--studio">
      <p class="venue__title">Personal Training</p>
      <p>Amberline Fitness Studio</p>
      <p>518 Wrenhollow Street</p>
      <p>Westhaven WA 6027</p>
    </div>
    <div class="venue venue--outdoor">
      <p class="venue__title">Outdoor Group Training</p>
      <p>Ferndale Archers Club</p>
      <p>42 Tillbrook Road</p>
      <p>Westhaven WA 6027</p>
    </div>
  </section>

  <section class="card card--front" aria-label="Front of card">
    <div class="brand-mark">
      <span class="brand-mark__dot"></span>
      <span class="brand-mark__name">KINETRIXX FITNESS</span>
    </div>
    <div class="contact">
      <p class="contact__name">Gareth Pollwick</p>
      <p class="contact__role">Director</p>
      <ul class="contact__list">
        <li class="contact__item">
          <svg class="contact__icon" viewBox="0 0 16 16" aria-hidden="true"><path d="M1 5c0-2 3-3 7-3s7 1 7 3v1h-4V4.5H5V6H1zM3 7h10l1 7H2z"/></svg>
          0458 702 136
        </li>
        <li class="contact__item">
          <svg class="contact__icon" viewBox="0 0 16 16" aria-hidden="true"><path d="M1 3h14v10H1zM2.5 4.5 8 9l5.5-4.5" fill="none" stroke="#e8322b" stroke-width="1.6"/></svg>
          kinetrixx@postnest.com
        </li>
        <li class="contact__item">
          <svg class="contact__icon" viewBox="0 0 16 16" aria-hidden="true"><g fill="none" stroke="#e8322b" stroke-width="1.4"><circle cx="8" cy="8" r="6.5"/><ellipse cx="8" cy="8" rx="3" ry="6.5"/><path d="M1.5 8h13M3 4.5h10M3 11.5h10"/></g></svg>
          kinetrixxfitness.com.au
        </li>
      </ul>
    </div>
    <p class="abn">ABN : 48392057</p>
  </section>

</main>
</body>
</html>
```